Real Estate flyer for listing properties

This is a flyer to be used by the property lister (the person trying to convince property vendors to sell through us) of our real estate agency Golden Harbour (https://www.golden-harbour.example). The aim of the flyer is to convince owners to list their properties with us, so that we can advertise & sell them. We have our offices located in San Luis de Sabinillas / Manilva, Costa del Sol, Spain. The real estate market here is highly competetive and we want to stand out from our competition and establish trust, which is essential for owners to list with us.

I have attached the design of our old flyer. Please note that we would like the new flyer to use our new logo, and our colors, not the wine red color used previously

I have also added some photos of our offices and of properties we have sold. We can provide more photos on request.

1. Project Overview & Objectives
High-level goal: Convince owners in Manilva & nearby to list with us.

2. Style guidelines
Please stick with the current logo & Font. We do NOT require a logo re-design. The font for Golden Harbour is Myriad Pro Bold Italic in color #D1672E. The blue used is #65A8DE and yellow #F2E946
The flyer should be A5 size.

3. Mandatory elements
Section with agent photo, name, email address & phone number. The design should allow for the flyer to be two sided, where one side is in English, and the other side in Spanish.

4. Ideas
- Maybe include address of offices (Calle Los Pinos 8, 29601 San Luis de Sabinillas) or QR code to open on google
- Offer free valuations
- Maybe mention biggest portals we are on with logo e.g. Casaverde, Vivilar, Techos.example, Moravo, A Home By the Bay, etc
- List languages we speak (Spanish, English, German, Russian, Ukrainian, Lithuanian, French, Italian, Danish, Polish)
- We also offer: Maintenance & Key holding
- Mention we have clients waiting
Note, these are just ideas, obviously not everything can be on the flyer.

Please note that the final flyer should be good for printing, just to be updated with the agents picture and contact details. Meaning all the marketing text should be written.

5. Assets & Output
Output sizes: e.g. A5 print flyer (210 × 148 mm), plus a social-media optimized JPG (1080 × 1080 px).

File formats required: InDesign (editable), plus flattened PDF for print; JPG/PNG for web.

5. Additional task - "stationary"
We need a design for a flap folder. I have attached a photo of such a flap folder, as well as the illustrator printing guidelines from the printing company.

Feel free to message me in case you have any questions or doubts.

Industry/Entity Type

Real Estate

Requirements
Must have
• Use our company logo, color scheme (from logo)

```html
<!DOCTYPE html>
<html lang="en">
<head>
<meta charset="utf-8">
<title>Golden Harbour – Listing Flyer</title>
<link rel="stylesheet" href="https://fonts.googleapis.com/css2?family=Montserrat:ital,wght@0,400;0,500;0,700;1,400;1,500;1,700&display=swap">
<style>
  :root {
    --brand-orange: #D1672E;
    --bar-orange: #EE6A2A;
    --brand-blue: #65A8DE;
    --stripe-blue: #2BA8E0;
    --brand-yellow: #F2E946;
    --ink: #111111;
    --ink-soft: #3a3a3a;
    --muted: #555555;
    --paper: #ffffff;
    --backdrop: #e9e9e9;
  }
  * { margin: 0; padding: 0; box-sizing: border-box; }
  html, body { width: 1200px; height: 1200px; overflow: hidden; }
  body {
    background: var(--backdrop);
    font-family: "Montserrat", Arial, sans-serif;
    color: var(--ink);
    position: relative;
  }
  .flyer {
    position: absolute;
    left: 213px; top: 52px;
    width: 774px; height: 1096px;
    background: var(--paper);
    overflow: hidden;
  }
  .hero { position: absolute; left: 0; top: 0; width: 774px; height: 520px; }

  .brand {
    position: absolute; left: 0; top: 540px; width: 774px;
    display: flex; justify-content: center; align-items: center; gap: 22px;
  }
  .brand-mark {
    width: 96px; height: 96px; border-radius: 50%;
    background: var(--brand-yellow);
    flex: none;
  }
  .brand-name {
    font-weight: 700; font-size: 33px; color: var(--brand-orange);
    line-height: 1.1;
  }
  .brand-regions { font-size: 17px; color: var(--muted); margin-top: 4px; }
  .brand-web { font-size: 20px; color: var(--ink-soft); margin-top: 4px; }

  .offer { position: absolute; left: 0; width: 774px; text-align: center; }
  .offer-intro { top: 694px; font-size: 27px; font-style: italic; color: var(--ink-soft); }
  .offer-title { top: 734px; font-size: 35px; font-weight: 700; letter-spacing: 0.5px; }

  .clients-badge {
    position: absolute; left: 213px; top: 804px; width: 346px; height: 40px;
    background: var(--brand-yellow);
    border-radius: 20px 6px 20px 6px;
    transform: skewX(-12deg);
    display: flex; align-items: center; justify-content: center;
  }
  .clients-badge span {
    transform: skewX(12deg);
    font-size: 21px; font-style: italic; font-weight: 500; color: var(--ink-soft);
  }

  .footer-band { position: absolute; left: 0; top: 1008px; width: 774px; height: 88px; z-index: 1; }
  .agent-photo {
    position: absolute; left: 24px; top: 895px; width: 166px; height: 181px;
    background: #000; z-index: 2;
  }
  .agent-details {
    position: absolute; left: 211px; top: 975px; font-style: italic; z-index: 2;
    line-height: 1.25;
  }
  .agent-name { font-size: 19px; font-weight: 700; }
  .agent-line { font-size: 15px; color: var(--ink-soft); }

  .office-address {
    position: absolute; right: 44px; top: 944px; text-align: right;
    font-size: 17px; line-height: 1.4; color: var(--ink-soft); font-style: normal;
  }
  .footer-web {
    position: absolute; right: 44px; top: 1024px; z-index: 2;
    font-size: 17px; font-weight: 700; color: var(--ink);
  }
</style>
</head>
<body>
  <main class="flyer">
    <svg class="hero" viewBox="0 0 774 520">
      <defs>
        <linearGradient id="heroTone" x1="0" y1="0" x2="0" y2="1">
          <stop offset="0" stop-color="#cfe3f3"/>
          <stop offset="0.35" stop-color="#eef0ee"/>
          <stop offset="0.6" stop-color="#d9ddd6"/>
          <stop offset="0.72" stop-color="#6bbfe6"/>
          <stop offset="1" stop-color="#1f9bd8"/>
        </linearGradient>
      </defs>
      <path role="img" aria-label="Photo of a white apartment complex with a swimming pool under a clear sky"
            d="M0 0 H774 V360 C660 460 500 505 386 499 C250 490 120 424 0 424 Z"
            fill="url(#heroTone)"/>
      <path d="M0 428 C120 430 250 480 370 497 C250 506 110 486 0 478 Z" fill="var(--bar-orange)"/>
      <path d="M0 424 C120 424 250 490 386 499 C500 505 660 460 774 360"
            fill="none" stroke="var(--brand-yellow)" stroke-width="9"/>
    </svg>

    <header class="brand">
      <div class="brand-mark"></div>
      <div class="brand-text">
        <div class="brand-name">Golden Harbour</div>
        <div class="brand-regions">Marbella Estepona Sotogrande</div>
        <div class="brand-web">www.golden-harbour.example</div>
      </div>
    </header>

    <p class="offer offer-intro">We also offer:</p>
    <h1 class="offer offer-title">MAINTENANCE &amp; KEY HOLDING</h1>
    <div class="clients-badge"><span>we have clients waiting</span></div>

    <svg class="footer-band" viewBox="0 0 774 88" aria-hidden="true">
      <polygon points="475,0 500,0 470,56 445,56" fill="var(--stripe-blue)"/>
      <polygon points="500,0 774,0 774,56 470,56" fill="var(--bar-orange)"/>
      <rect x="0" y="56" width="774" height="32" fill="var(--bar-orange)"/>
    </svg>

    <div class="agent-photo" role="img" aria-label="Agent photo placeholder"></div>
    <div class="agent-details">
      <div class="agent-name">AGENT NAME</div>
      <div class="agent-line">1234 567 890</div>
      <div class="agent-line">info@golden-harbour.example</div>
    </div>

    <address class="office-address">
      Calle Los Pinos 8,<br>29601 San Luis de Sabinillas
    </address>

    <div class="footer-web">www.golden-harbour.example</div>
  </main>
</body>
</html>
```